BrookfieldVentures Business Card Design

Design business cards with attached ideas. I am open to several different ideas that would be interesting and innovative. What I have provided is logo and colors. Font should be Helvetica although it could be bold or light as needed. The design can be vertical or horizontal. The design should be more interesting than a standard business card. Files must be ready to send to a printer and in Illustrator format. The text with the five icons should be exact. Send me some ideas and I will get back to you right away. I need to choose a design within 3-5 days.

Target Market(s)

Business audience

Industry/Entity Type

Business

Contact Information for Business Card

Files should be ready to send to printer in illustrator format

Font styles to use
Sans Serif

Colors
3276b5

Requirements
Must have
• Use attached logo and two colors - blue / gray
• Include 5 offering icons and text on back
Nice to have
• Interesting and innovative design. Vertical or horizontal are both fine.

```html
<!DOCTYPE html>
<html lang="en">
<head>
<meta charset="utf-8">
<title>BrookfieldVentures Business Card</title>
<link rel="stylesheet" href="https://fonts.googleapis.com/css2?family=Open+Sans:wght@400;600;700&display=swap">
<style>
  :root {
    --blue: #3276b5;
    --blue-deep: #2a5f93;
    --gray: #4a4a4a;
    --gray-mid: #6b6b6b;
    --card: #efeeeb;
    --backdrop: #e4e4e2;
  }
  * { box-sizing: border-box; margin: 0; padding: 0; }
  html, body {
    width: 1200px; height: 800px; overflow: hidden;
    background: var(--backdrop);
    font-family: "Open Sans", Helvetica, Arial, sans-serif;
  }
  .stage { position: relative; width: 1200px; height: 800px; }
  .card {
    position: absolute; width: 525px; height: 300px;
    background: var(--card);
    box-shadow: 0 2px 6px rgba(0,0,0,.12);
    overflow: hidden;
  }
  .card--back { left: 45px; top: 250px; border-left: 4px solid var(--blue); }
  .card--front { left: 630px; top: 250px; }

  /* back */
  .back__mark {
    position: absolute; right: 26px; top: 22px;
    width: 40px; height: 40px; background: var(--blue);
  }
  .offerings { position: absolute; left: 34px; top: 80px; }
  .offerings__title {
    font-size: 16px; font-weight: 700; color: var(--gray);
    margin-bottom: 12px; line-height: 22px;
  }
  .offerings__title .accent { color: var(--blue); }
  .offerings__list { list-style: none; }
  .offering {
    display: flex; align-items: center; gap: 12px;
    font-size: 11.5px; font-weight: 700; color: var(--gray);
    margin-bottom: 6px;
  }
  .offering:last-child { margin-bottom: 0; }
  .offering__icon {
    width: 25px; height: 25px; border-radius: 50%;
    background: var(--blue); flex: none;
    display: flex; align-items: center; justify-content: center;
  }

  /* front */
  .brand { position: absolute; left: 34px; top: 178px; }
  .brand__row { display: flex; align-items: center; gap: 8px; }
  .brand__square { width: 28px; height: 28px; background: var(--blue); flex: none; }
  .brand__name { font-size: 17px; font-weight: 700; color: var(--blue); letter-spacing: -.2px; }
  .brand__tagline { font-size: 9px; font-weight: 600; color: var(--gray); margin: 3px 0 0 36px; }
  .divider {
    position: absolute; left: 272px; top: 40px; width: 1.5px; height: 220px;
    background: var(--blue);
  }
  .person { position: absolute; left: 292px; top: 70px; right: 16px; }
  .person__name { font-size: 18px; font-weight: 700; color: var(--gray); letter-spacing: .2px; white-space: nowrap; }
  .person__role { font-size: 13px; color: var(--blue); margin-bottom: 10px; }
  .contact { list-style: none; }
  .contact__item {
    display: flex; align-items: center; gap: 7px;
    font-size: 11px; color: var(--gray-mid); margin-bottom: 3px;
  }
  .contact__item svg { flex: none; fill: var(--blue-deep); }
</style>
</head>
<body>
<main class="stage">

  <section class="card card--back" aria-label="Card back">
    <div class="back__mark"></div>
    <div class="offerings">
      <h2 class="offerings__title"><span class="accent">Brookfield</span> Ventures Offerings</h2>
      <ul class="offerings__list">
        <li class="offering">
          <span class="offering__icon"><svg width="13" height="13" viewBox="0 0 13 13" fill="none" stroke="#fff" stroke-width="1.3"><rect x="1.5" y="1.5" width="10" height="10"/><path d="M4 5h5M4 7h5M4 9h3"/></svg></span>
          Concepts: Thought leadership white papers
        </li>
        <li class="offering">
          <span class="offering__icon"><svg width="13" height="13" viewBox="0 0 13 13" fill="#fff"><circle cx="6.5" cy="3.5" r="2"/><rect x="3" y="6.5" width="7" height="3" rx="1"/><rect x="1" y="10" width="11" height="1.5"/></svg></span>
          Curriculum: Short courses on strategy
        </li>
        <li class="offering">
          <span class="offering__icon"><svg width="14" height="13" viewBox="0 0 14 13" fill="#fff"><circle cx="3.5" cy="3" r="1.8"/><circle cx="10.5" cy="3" r="1.8"/><rect x="1.5" y="5.5" width="4" height="6"/><rect x="8.5" y="5.5" width="4" height="6"/></svg></span>
          Coaching: Building your strategic leadership
        </li>
        <li class="offering">
          <span class="offering__icon"><svg width="14" height="13" viewBox="0 0 14 13" fill="#fff" stroke="#fff" stroke-width="1"><circle cx="7" cy="2.5" r="1.8"/><circle cx="2.5" cy="10.5" r="1.8"/><circle cx="11.5" cy="10.5" r="1.8"/><path d="M7 4.5v2.5M2.5 8.5V7h9v1.5" fill="none"/></svg></span>
          Consulting: Developing your strategic future
        </li>
        <li class="offering">
          <span class="offering__icon"><svg width="14" height="13" viewBox="0 0 14 13" fill="none" stroke="#fff" stroke-width="1.3"><rect x="2" y="1.5" width="10.5" height="7.5"/><path d="M4 7l2.5-2.5 2 1.5L11 3.5M7 9v3"/></svg></span>
          ScoreCard: Balanced ScoreCard and software
        </li>
      </ul>
    </div>
  </section>

  <section class="card card--front" aria-label="Card front">
    <div class="brand">
      <div class="brand__row">
        <span class="brand__square"></span>
        <span class="brand__name">BrookfieldVentures</span>
      </div>
      <p class="brand__tagline">Clear Plans - Steady Growth</p>
    </div>
    <div class="divider"></div>
    <div class="person">
      <h1 class="person__name">DANA WHITLOCK, PhD</h1>
      <p class="person__role">Managing Director</p>
      <ul class="contact">
        <li class="contact__item">
          <svg width="10" height="10" viewBox="0 0 10 10"><path d="M2 0.5l2 2-1 1.2c.6 1.3 1.5 2.2 2.8 2.8l1.2-1 2 2-1.3 1.7C4.5 9 1 5.5.3 1.8z"/></svg>
          555 - 014 - 0372
        </li>
        <li class="contact__item">
          <svg width="11" height="9" viewBox="0 0 11 9"><path d="M0 0h11v1.5L5.5 5 0 1.5zM0 3l5.5 3.5L11 3v6H0z"/></svg>
          dana@brookfieldventures.com
        </li>
        <li class="contact__item">
          <svg width="10" height="11" viewBox="0 0 10 11"><path d="M1 0l8 6-3.3.6L8 10l-1.6.9L4.2 7.4 1 10z"/></svg>
          BrookfieldVentures.com
        </li>
      </ul>
    </div>
  </section>

</main>
</body>
</html>
```